Bluefern painting and decorating *

Need a flyer design to advertise my services
So the information I need included is the services we offer at bluefern painting and decorating which include
Interior painting
Exterior painting
Wallpaper hanging
Paint and cellulose spraying
Dust free sanding
Pressure washing
Stone cleaning
Also would need to have my company contact details in
Www.bluefernpaintingdecorating.co.uk
Email is info@bluefernpaintingdecorating.com
Bluefern Painting & Decorating Services has a proven track record of innovative designs, effective problem solving and attention to detail and our goal is to meet and exceed the expectations of every customer. We take on all types of jobs from small domestic work to larger commercial projects, all carried out to the highest standards, and at very competitive prices.

```html
<!DOCTYPE html>
<html lang="en">
<head>
<meta charset="utf-8">
<title>Bluefern painting and decorating – Flyer</title>
<link href="https://fonts.googleapis.com/css2?family=Open+Sans:wght@300;400;600;700;800&display=swap" rel="stylesheet">
<style>
:root{
  --page:#c9c9cb;
  --white:#ffffff;
  --blue:#2c74c2;
  --sky:#3497d6;
  --navy:#0f3a66;
  --deep:#1b5692;
  --ink:#1d3f6e;
  --grey-text:#9aa3ad;
  --list-bg:#eef0f3;
  --footer:#3a3b3d;
  --gold:#f2c230;
}
*{box-sizing:border-box;margin:0;padding:0}
html,body{width:1200px;height:960px;overflow:hidden}
body{background:var(--page);font-family:"Open Sans",Arial,sans-serif;position:relative}
.flyer{position:absolute;left:280px;top:27px;width:640px;height:906px;background:var(--white);overflow:hidden;box-shadow:0 10px 30px rgba(0,0,0,.25)}
.abs{position:absolute}

/* header */
.header{left:0;top:0;width:640px;height:88px}
.brand{left:26px;top:26px;display:flex;align-items:center;gap:8px;width:190px}
.brand-mark{flex:none;width:16px;height:16px;background:var(--blue)}
.brand-name{font-weight:700;font-size:14px;line-height:1.2;color:var(--ink)}
.contact{right:24px;top:34px;display:flex;gap:20px;font-size:11px;color:#222;white-space:nowrap}
.contact-item{display:flex;align-items:center;gap:6px}
.contact-icon{width:18px;height:18px;background:var(--blue);display:flex;align-items:center;justify-content:center}
.rule{left:0;width:640px;height:9px;border-top:4px solid var(--blue);border-bottom:2px solid var(--blue)}

/* hero */
.hero{left:0;top:98px;width:640px;height:292px;background:linear-gradient(135deg,#6d6a66 0%,#b7b5b2 35%,#d9d8d6 60%,#8b8178 100%)}
.hero-shade{left:0;top:98px;width:640px;height:292px;background:linear-gradient(180deg,rgba(0,0,0,0) 30%,rgba(0,0,0,.35) 100%)}
.hero-text{left:40px;top:190px;width:560px;color:var(--white);text-align:center}
.hero-title{font-weight:800;font-size:36px;line-height:1.05}
.hero-sub{font-weight:400;font-size:30px;line-height:1.2}
.hero-body{margin-top:14px;font-size:11.5px;line-height:1.5}

/* services */
.col-head{top:398px;height:44px;color:var(--white);font-size:17px;display:flex;align-items:center;justify-content:center}
.domestic-head{left:0;width:320px;background:var(--sky)}
.commercial-head{left:320px;width:320px;background:var(--deep)}
.photo{top:442px;height:104px}
.domestic-photo{left:0;width:320px;background:linear-gradient(90deg,#e8b83a 0%,#d99d2e 45%,#2f4a5e 60%,#26384a 100%)}
.commercial-photo{left:320px;width:320px;background:linear-gradient(90deg,#9cc6df 0%,#5b88a8 45%,#c7a57a 70%,#8d7259 100%)}
.list-area{top:546px;height:178px;background:linear-gradient(180deg,var(--list-bg),#f8f9fa)}
.domestic-list-area{left:0;width:320px}
.commercial-list-area{left:320px;width:320px}
.service-list{list-style:none;color:var(--grey-text);font-size:15px;line-height:1.42;font-weight:400}
.domestic-list{left:38px;top:556px}
.commercial-list{left:356px;top:556px}
.why{left:352px;top:722px;width:260px;text-align:center}
.why-title{font-weight:800;font-size:25px;color:var(--navy)}
.why-line{margin:2px auto 0;width:200px;height:2px;background:var(--navy)}

/* reasons */
.reasons{left:0;top:762px;width:640px;height:60px;display:flex}
.reason{flex:1;display:flex;flex-direction:column;align-items:center;justify-content:center;gap:5px;color:var(--white);font-size:10.5px;font-weight:700}
.r-exp{background:var(--blue)}
.r-craft{background:var(--navy)}
.r-price{background:var(--blue)}

/* footer */
.footer{left:0;top:822px;width:640px;height:84px;background:var(--footer)}
.socials{left:26px;top:848px;display:flex;gap:10px}
.social{width:28px;height:28px;border-radius:50%}
.s1{background:#36507e}.s2{background:#2e8fd6}.s3{background:#1d64a3}.s4{background:#2aa34a}
.s5{background:#6a6b6d;display:flex;align-items:center;justify-content:center}
.quote{left:236px;top:838px;width:180px;text-align:center;color:var(--white)}
.quote-label{font-size:11px;font-weight:700}
.quote-box{margin-top:3px;border:1px solid #ddd;padding:4px 0;font-size:18px;font-weight:400}
.review{left:470px;top:838px;color:var(--white);text-align:center}
.review-label{font-size:8px;color:#ccc}
.review-badge{display:flex;align-items:center;gap:6px;margin-top:3px;font-size:16px}
.review-shape{width:14px;height:14px;background:var(--gold)}
.stars{margin-top:3px;color:var(--gold);font-size:13px;letter-spacing:3px}
</style>
</head>
<body>
<div class="flyer">
  <header class="abs header">
    <div class="abs brand"><span class="brand-mark"></span><span class="brand-name">Bluefern painting<br>and decorating</span></div>
    <div class="abs contact">
      <div class="contact-item">
        <span class="contact-icon"><svg width="11" height="11" viewBox="0 0 24 24"><path fill="#fff" d="M6.6 10.8a15 15 0 0 0 6.6 6.6l2.2-2.2c.3-.3.7-.4 1-.2 1.1.4 2.3.6 3.6.6.6 0 1 .4 1 1V20c0 .6-.4 1-1 1A17 17 0 0 1 3 4c0-.6.4-1 1-1h3.5c.6 0 1 .4 1 1 0 1.3.2 2.5.6 3.6.1.3 0 .7-.2 1z"/></svg></span>
        07700 900 417
      </div>
      <div class="contact-item">
        <span class="contact-icon"><svg width="11" height="9" viewBox="0 0 22 16"><rect x="1" y="1" width="20" height="14" fill="none" stroke="#fff" stroke-width="2"/><path d="M1 1l10 8 10-8" fill="none" stroke="#fff" stroke-width="2"/></svg></span>
        info@bluefernpaintingdecorating.com
      </div>
    </div>
  </header>
  <div class="abs rule" style="top:88px"></div>

  <div class="abs hero" role="img" aria-label="Photo of a bright, freshly decorated open-plan living room"></div>
  <div class="abs hero-shade"></div>
  <div class="abs hero-text">
    <div class="hero-title">Established decorators</div>
    <div class="hero-sub">in South London</div>
    <p class="hero-body">Get in touch with our expert decorators at Bluefern Painting and Decorating Services in Bexley to give your property a makeover. Our services are available across South London.</p>
  </div>
  <div class="abs rule" style="top:389px"></div>

  <div class="abs col-head domestic-head">Domestic Services</div>
  <div class="abs col-head commercial-head">Commercial Services</div>
  <div class="abs photo domestic-photo" role="img" aria-label="Photos of decorated domestic living rooms"></div>
  <div class="abs photo commercial-photo" role="img" aria-label="Photos of decorated commercial office interiors"></div>
  <div class="abs list-area domestic-list-area"></div>
  <div class="abs list-area commercial-list-area"></div>

  <ul class="abs service-list domestic-list">
    <li>Interior painting</li>
    <li>Exterior painting</li>
    <li>Wallpaper hanging</li>
    <li>Paint and cellulose spraying</li>
    <li>Dust free sanding</li>
    <li>Pressure washing</li>
    <li>Stone cleaning</li>
  </ul>
  <ul class="abs service-list commercial-list">
    <li>Interior painting</li>
    <li>Exterior painting</li>
    <li>Paint and cellulose spraying</li>
    <li>Dust free sanding</li>
    <li>Pressure washing</li>
    <li>Stone cleaning</li>
  </ul>

  <div class="abs why"><div class="why-title">Why choose us?</div><div class="why-line"></div></div>

  <div class="abs reasons">
    <div class="reason r-exp">
      <svg width="20" height="22" viewBox="0 0 20 22"><circle cx="10" cy="8" r="6" fill="none" stroke="#fff" stroke-width="1.5"/><path d="M6 13l-2 8 4-2 2 2 0-6M14 13l2 8-4-2" fill="none" stroke="#fff" stroke-width="1.5"/></svg>
      Over 12 years of experience
    </div>
    <div class="reason r-craft">
      <svg width="22" height="22" viewBox="0 0 22 22"><circle cx="11" cy="11" r="9.5" fill="none" stroke="#fff" stroke-width="1.5"/><path d="M7 11l3 3 5-6" fill="none" stroke="#fff" stroke-width="1.5"/></svg>
      Quality craftsmanship
    </div>
    <div class="reason r-price">
      <svg width="22" height="22" viewBox="0 0 22 22"><circle cx="11" cy="11" r="9.5" fill="none" stroke="#fff" stroke-width="1.5"/><text x="11" y="15.5" text-anchor="middle" font-size="12" fill="#fff" font-family="Open Sans, sans-serif">£</text></svg>
      Competitive prices
    </div>
  </div>

  <footer class="abs footer"></footer>
  <div class="abs socials">
    <span class="social s1"></span><span class="social s2"></span><span class="social s3"></span><span class="social s4"></span>
    <span class="social s5"><svg width="14" height="10" viewBox="0 0 22 16"><rect x="1" y="1" width="20" height="14" fill="none" stroke="#fff" stroke-width="2"/><path d="M1 1l10 8 10-8" fill="none" stroke="#fff" stroke-width="2"/></svg></span>
  </div>
  <div class="abs quote">
    <div class="quote-label">free quote</div>
    <div class="quote-box">07700 900 417</div>
  </div>
  <div class="abs review">
    <div class="review-label">Review us on</div>
    <div class="review-badge"><span class="review-shape"></span>Listwise</div>
    <div class="stars">★★★★★</div>
  </div>
</div>
</body>
</html>
```